Halvorn - Refresh the look and feel of an existing website

We currently have an existing website www.halvornworldadvisory.example however it needs a more refreshed 'look and feel'. We are a professional consultancy that works with large corporate organisations and government. Our 'tag line' is A New Way of Thinking. We want the site to communicate "Innovation" and Leading Edge Thinking.

Target Market(s)

Corporate and Professional Clients - Organisation and Business Change

Industry/Entity Type

Management Consulting

Number of Pages Required

1 page

Font styles to use
Sans Serif

Requirements
Must have
• Must have a professional Corporate look and feel. Header 'imagery' is ok but boxes on front page need changing ... along with the words. The focus on home page needs to 'call out' 3 main consulting areas:-
• - Change & Transformation Specialists
• - Innovative Solutions
• - Digital Transformation
• Tag Line for business is ... A New Way of Thinking (Highlighting Halvorn as 'Thought Leaders' in business)
Nice to have
• Less "words' more imagery. Possibly an area for a 'video' or recent articles/blogs on the front page. Needs to have more of an 'interactive' feel. We are open to suggestions.
Should not have
• NA

```html
<!DOCTYPE html>
<html lang="en">
<head>
<meta charset="utf-8">
<title>Halvorn – A New Way of Thinking</title>
<link href="https://fonts.googleapis.com/css2?family=Open+Sans:ital,wght@0,300;0,400;0,600;0,700;1,400;1,600&display=swap" rel="stylesheet">
<style>
:root{
  --navy:#1f3551;
  --navy-deep:#162739;
  --ink:#2b2f36;
  --muted:#6b717a;
  --line:#d6dae0;
  --panel:#eceef1;
  --panel-soft:#f4f5f7;
  --white:#ffffff;
  --accent:#3d78b5;
}
*{box-sizing:border-box;margin:0;padding:0}
html,body{width:752px;height:1200px;overflow:hidden}
body{font-family:"Open Sans",Arial,sans-serif;color:var(--ink);background:var(--white);position:relative}

/* header */
.site-header{position:absolute;left:0;top:0;width:752px;height:62px;background:var(--white);border-bottom:1px solid var(--line)}
.brand{position:absolute;left:40px;top:14px;display:flex;align-items:center;gap:8px}
.brand-mark{width:30px;height:30px;border-radius:50%;background:var(--navy)}
.brand-name{font-size:20px;font-weight:700;color:var(--navy);letter-spacing:1px}
.header-phone{position:absolute;right:36px;top:6px;font-size:10px;font-weight:600;color:var(--navy);display:flex;align-items:center;gap:4px}
.main-nav{position:absolute;right:36px;top:32px;display:flex;gap:4px}
.main-nav a{font-size:9.5px;color:var(--ink);text-decoration:none;padding:4px 11px;border:1px solid transparent;border-radius:2px}
.main-nav a.is-active{border-color:var(--line);background:var(--panel-soft)}

/* hero */
.hero{position:absolute;left:0;top:62px;width:752px;height:388px;
  background:
    radial-gradient(ellipse 180px 140px at 400px 110px,rgba(235,243,252,.85),rgba(235,243,252,0) 70%),
    radial-gradient(ellipse 220px 160px at 110px 80px,rgba(160,190,220,.7),rgba(160,190,220,0) 70%),
    radial-gradient(ellipse 200px 260px at 620px 150px,rgba(22,39,57,.85),rgba(22,39,57,0) 75%),
    radial-gradient(ellipse 260px 120px at 200px 250px,rgba(90,130,175,.6),rgba(90,130,175,0) 70%),
    linear-gradient(115deg,#b7cadf 0%,#7d9dc0 35%,#47668c 65%,#22384f 100%)}
.hero-tagline{position:absolute;left:0;top:165px;width:752px;text-align:center;font-size:26px;font-weight:300;color:var(--white);padding-left:90px;letter-spacing:.5px;text-shadow:0 1px 3px rgba(0,0,0,.3)}

.service-cards{position:absolute;left:100px;top:300px;width:552px;display:flex;gap:9px}
.service-card{width:178px;height:126px;background:var(--white);border:1px solid var(--line);box-shadow:0 2px 6px rgba(0,0,0,.15);position:relative}
.service-card .card-photo{height:80px;margin:4px;background:linear-gradient(135deg,#24466e,#5d86b3)}
.service-card:nth-child(1) .card-photo{background:linear-gradient(135deg,#0f2a4c,#3f73a6)}
.service-card:nth-child(3) .card-photo{background:linear-gradient(135deg,#1a3a5e,#8fb0d0)}
.card-title{position:absolute;left:4px;right:4px;bottom:4px;height:38px;display:flex;align-items:center;justify-content:center;text-align:center;font-size:10.5px;font-weight:400;line-height:1.25;color:var(--ink);padding-left:30px;padding-right:6px}
.card-icon{position:absolute;left:9px;top:73px;width:20px;height:20px;border-radius:50%;background:var(--white);border:2px solid var(--navy);z-index:2}
.service-card.is-featured .card-title{background:var(--navy);color:var(--white)}

/* welcome */
.welcome{position:absolute;left:0;top:458px;width:752px;height:202px;background:var(--panel)}
.welcome h2{position:absolute;left:100px;top:28px;font-size:18px;font-weight:400;color:var(--ink)}
.welcome h2 strong{color:var(--navy);font-weight:700;letter-spacing:1px}
.welcome p{position:absolute;left:100px;width:300px;font-size:8px;line-height:1.5;color:var(--muted)}
.welcome .intro{top:60px;color:var(--ink);font-weight:600}
.welcome .body{top:96px}
.btn-more{position:absolute;left:100px;top:150px;background:var(--navy);color:var(--white);font-size:8px;padding:5px 12px;border-radius:10px;text-decoration:none}
.video-panel{position:absolute;left:440px;top:20px;width:180px;height:160px;border-radius:6px;background:linear-gradient(160deg,#d8dde3,#9aa6b4)}

/* blog */
.blog{position:absolute;left:0;top:660px;width:752px;height:140px;background:var(--white)}
.section-title{position:absolute;left:0;width:752px;text-align:center;font-size:20px;font-weight:400;color:var(--navy)}
.blog .section-title{top:16px}
.blog-arrow{position:absolute;top:70px;width:16px;height:16px}
.blog-post{position:absolute;top:60px;width:250px;display:flex;gap:10px}
.post-photo{width:78px;height:54px;flex:none;background:linear-gradient(135deg,#3b5677,#9fb4ca)}
.post-text h3{font-size:8px;font-weight:600;color:var(--navy);margin-bottom:3px}
.post-text time{font-size:7px;color:var(--muted);display:block;margin-bottom:3px}
.post-text p{font-size:7px;line-height:1.45;color:var(--muted)}

/* testimonials */
.testimonials{position:absolute;left:0;top:800px;width:752px;height:230px;background:var(--panel-soft)}
.testimonials .section-title{top:16px}
.quote{position:absolute;left:120px;top:58px;width:512px;text-align:center;font-size:9px;font-style:italic;font-weight:600;line-height:1.5;color:var(--ink)}
.quote-mark{position:absolute;top:52px;font-size:24px;color:var(--navy);font-weight:700}
.client-name{position:absolute;left:0;top:102px;width:752px;text-align:center;font-size:8px;color:var(--muted)}
.client-photo{position:absolute;left:346px;top:120px;width:60px;height:60px;border-radius:50%;background:linear-gradient(160deg,#c9b9a8,#8f7e6e);border:3px solid var(--white);box-shadow:0 1px 4px rgba(0,0,0,.2)}
.dots{position:absolute;left:0;top:190px;width:752px;display:flex;justify-content:center;gap:5px}
.dots span{width:6px;height:6px;border-radius:50%;background:#b9bfc7}
.dots span.is-active{background:var(--navy)}

/* footer */
.site-footer{position:absolute;left:0;top:1010px;width:752px;height:178px}
.footer-shape{position:absolute;left:0;top:0}
.footer-col{position:absolute;top:40px;color:var(--white)}
.footer-col h4{font-size:10px;font-weight:600;margin-bottom:8px}
.footer-col ul{list-style:none}
.footer-col li{font-size:7.5px;line-height:1.9;color:#c8d2de}
.footer-col li::before{content:"› ";}
.inquiry-field{width:110px;height:12px;background:var(--white);border-radius:2px;margin-bottom:5px;font-size:6.5px;color:var(--muted);padding:1px 4px}
.inquiry-field.tall{height:26px}
.inquiry-send{display:inline-block;font-size:7px;background:var(--white);color:var(--navy);padding:2px 8px;border-radius:2px}
.contact-row{display:flex;align-items:center;gap:5px;font-size:7.5px;line-height:1.3;color:#c8d2de;margin-bottom:6px}
.contact-row svg{flex:none}
.footer-mark{position:absolute;left:612px;top:38px;width:64px;height:64px;border-radius:50%;border:3px solid #c8d2de}
.social{position:absolute;left:616px;top:118px;display:flex;gap:5px}
.social span{width:13px;height:13px;border-radius:50%;background:var(--accent)}
.social span:nth-child(2){background:#d84a3a}
.copyright{position:absolute;left:0;top:1188px;width:752px;height:12px;background:var(--navy-deep);color:#9fb0c3;font-size:6.5px;text-align:center;line-height:12px}
</style>
</head>
<body>

<header class="site-header">
  <div class="brand"><span class="brand-mark"></span><span class="brand-name">HALVORN</span></div>
  <div class="header-phone">
    <svg width="9" height="9" viewBox="0 0 24 24"><path fill="#1f3551" d="M6.6 10.8a15 15 0 006.6 6.6l2.2-2.2c.3-.3.7-.4 1-.2 1.1.4 2.3.6 3.6.6.6 0 1 .4 1 1V20c0 .6-.4 1-1 1A17 17 0 013 4c0-.6.4-1 1-1h3.5c.6 0 1 .4 1 1 0 1.3.2 2.5.6 3.6.1.3 0 .7-.2 1z"/></svg>
    1300 555 012
  </div>
  <nav class="main-nav">
    <a class="is-active" href="#">Home</a><a href="#">About Us</a><a href="#">Our Services</a><a href="#">Solutions</a><a href="#">Blog</a><a href="#">Contact Us</a>
  </nav>
</header>

<section class="hero" role="img" aria-label="Business person touching a glowing digital interface over a world map">
  <h1 class="hero-tagline">A New Way of Thinking</h1>
</section>

<div class="service-cards">
  <article class="service-card">
    <div class="card-photo" role="img" aria-label="Hands holding a glowing network globe"></div>
    <span class="card-icon"></span>
    <h3 class="card-title">Change &amp; Transformation<br>Specialists</h3>
  </article>
  <article class="service-card is-featured">
    <div class="card-photo" role="img" aria-label="Finger touching a digital innovation display"></div>
    <span class="card-icon"></span>
    <h3 class="card-title">Innovative<br>Solutions</h3>
  </article>
  <article class="service-card">
    <div class="card-photo" role="img" aria-label="Digital devices connected across a blue network"></div>
    <span class="card-icon"></span>
    <h3 class="card-title">Digital<br>Transformation</h3>
  </article>
</div>

<section class="welcome">
  <h2>Welcome to <strong>HALVORN</strong></h2>
  <p class="intro">We help large organisations and government agencies rethink how they work, bringing fresh ideas and practical change to every engagement.</p>
  <p class="body">Our consultants combine strategy, technology and people skills to lead transformation programs from first concept to lasting results. We partner closely with leaders to shape clear direction and build confidence across teams.</p>
  <a class="btn-more" href="#">Read More</a>
  <div class="video-panel" role="img" aria-label="Hands holding a tablet playing a company video"></div>
</section>

<section class="blog">
  <h2 class="section-title">Blog Posts</h2>
  <svg class="blog-arrow" style="left:78px" viewBox="0 0 16 16"><path d="M10 3L5 8l5 5" fill="none" stroke="#1f3551" stroke-width="2"/></svg>
  <article class="blog-post" style="left:108px">
    <div class="post-photo" role="img" aria-label="Consulting team meeting around a table"></div>
    <div class="post-text">
      <h3>Leading change in complex organisations</h3>
      <time>12 March</time>
      <p>Practical lessons on guiding teams through large scale change with clarity and purpose.</p>
    </div>
  </article>
  <article class="blog-post" style="left:392px">
    <div class="post-photo" role="img" aria-label="Colleagues reviewing work on a laptop"></div>
    <div class="post-text">
      <h3>Building a digital first strategy</h3>
      <time>28 February</time>
      <p>How leaders can align technology investment with real business outcomes and growth.</p>
    </div>
  </article>
  <svg class="blog-arrow" style="left:660px" viewBox="0 0 16 16"><path d="M6 3l5 5-5 5" fill="none" stroke="#1f3551" stroke-width="2"/></svg>
</section>

<section class="testimonials">
  <h2 class="section-title">Clients Testimonials</h2>
  <span class="quote-mark" style="left:104px">“</span>
  <p class="quote">The team brought real insight to our transformation program. Their fresh thinking, steady guidance and focus on our people made the change smooth, and the results have lasted well beyond the project itself.</p>
  <span class="quote-mark" style="left:638px">”</span>
  <p class="client-name">Clara Wendell, Director</p>
  <div class="client-photo" role="img" aria-label="Portrait of the client"></div>
  <div class="dots"><span class="is-active"></span><span></span><span></span></div>
</section>

<footer class="site-footer">
  <svg class="footer-shape" width="752" height="178" viewBox="0 0 752 178" aria-hidden="true">
    <path d="M0 20 Q376 -18 752 20 V178 H0 Z" fill="#1f3551"/>
  </svg>
  <div class="footer-col" style="left:60px">
    <h4>Quick Links</h4>
    <ul><li>Home</li><li>About Us</li><li>Our Services</li><li>Solutions</li><li>Blog</li><li>Contact Us</li></ul>
  </div>
  <div class="footer-col" style="left:210px">
    <h4>Quick Inquiry</h4>
    <div class="inquiry-field">Name</div>
    <div class="inquiry-field">Email</div>
    <div class="inquiry-field tall">Message</div>
    <span class="inquiry-send">Send</span>
  </div>
  <div class="footer-col" style="left:385px">
    <h4>Contact Details</h4>
    <div class="contact-row"><svg width="9" height="9" viewBox="0 0 24 24"><path fill="#c8d2de" d="M12 2a7 7 0 00-7 7c0 5 7 13 7 13s7-8 7-13a7 7 0 00-7-7zm0 9.5A2.5 2.5 0 1112 6a2.5 2.5 0 010 5.5z"/></svg>Level 4, 22 Marlow Street,<br>Eastbridge</div>
    <div class="contact-row"><svg width="9" height="9" viewBox="0 0 24 24"><path fill="#c8d2de" d="M6.6 10.8a15 15 0 006.6 6.6l2.2-2.2c.3-.3.7-.4 1-.2 1.1.4 2.3.6 3.6.6.6 0 1 .4 1 1V20c0 .6-.4 1-1 1A17 17 0 013 4c0-.6.4-1 1-1h3.5c.6 0 1 .4 1 1 0 1.3.2 2.5.6 3.6.1.3 0 .7-.2 1z"/></svg>1300 555 012</div>
    <div class="contact-row"><svg width="9" height="9" viewBox="0 0 24 24"><path fill="#c8d2de" d="M3 5h18v14H3z"/></svg>1300 555 013</div>
    <div class="contact-row"><svg width="9" height="9" viewBox="0 0 24 24"><path fill="#c8d2de" d="M2 5h20v14H2zm2 2v.5l8 5 8-5V7z"/></svg>info@halvornworldadvisory.example</div>
  </div>
  <div class="footer-mark"></div>
  <div class="social"><span></span><span></span><span></span></div>
</footer>

<div class="copyright">Copyright © 2024 · Halvorn · All Rights Reserved</div>

</body>
</html>
```